Logo redesign & Stationery Design Project

We need a logo redesign for our company.

We also require the following stationary with the new logo:
*letterhead
*With compliments slips
*business card
*envelopes

We would like to maintain our current colours of navy blue and gold. We would like to maintain the wording on the back of our current business card.

Our existing letterhead and business card is attached.

Target Market(s)

Medical Professionals, Pharmacists, Lawyers

Industry/Entity Type

Business

Requirements
Must have
• See attached business card and letterhead, as all details on these documents need to be included.

```html
<!DOCTYPE html>
<html lang="en">
<head>
<meta charset="utf-8">
<title>Halden Marsh Financial Services — Stationery</title>
<link rel="stylesheet" href="https://fonts.googleapis.com/css2?family=Open+Sans:wght@400;600&family=Arimo&family=Great+Vibes&family=Cormorant+Garamond:ital,wght@1,500&display=swap">
<style>
:root{
  --navy:#12106e;
  --gold:#c99a12;
  --paper:#ffffff;
  --ink:#222222;
  --stage:#e9e6e1;
}
*{box-sizing:border-box;margin:0;padding:0}
html,body{width:1200px;height:1000px;overflow:hidden;background:var(--stage)}
body{position:relative;font-family:'Open Sans',sans-serif;color:var(--ink)}
.sheet{position:absolute;background:var(--paper);overflow:hidden;box-shadow:0 1px 4px rgba(0,0,0,.18)}

.brand{position:absolute;display:flex;align-items:center;gap:7px;color:var(--navy);font-family:'Open Sans',sans-serif;font-weight:400;line-height:1.05}
.brand__mark{width:22px;height:22px;background:var(--gold);flex:none}
.brand__name{font-size:19px}
.brand__sub{font-size:12px;display:block}

.contact{position:absolute;font-size:5.6px;line-height:1.45;color:var(--gold);padding-left:0}
.contact b{color:var(--navy);font-weight:600}
.rule{position:absolute;width:3px;background:var(--navy)}

/* letterhead */
.letterhead{left:53px;top:43px;width:518px;height:666px}
.letterhead .brand{left:18px;top:24px}
.letterhead .contact{left:382px;top:17px}
.letterhead .rule{left:511px;top:17px;height:44px}
.letter{position:absolute;left:8px;top:124px;font-family:'Arimo',sans-serif;font-size:9.6px;line-height:11.4px;color:var(--ink)}
.letter__greet{margin-bottom:6px}
.letter__para{margin-left:77px;width:386px;margin-bottom:11px}
.letter__sign{font-family:'Great Vibes',cursive;font-size:26px;margin:14px 0 0 30px;color:#111;line-height:1}
.letter__role{margin-left:48px;font-size:9px}
.band{position:absolute;left:0;right:0;background:var(--navy);color:#fff;font-size:8.5px;text-align:center;line-height:14px}
.letterhead .band{top:643px;height:14px}

/* business card back */
.card-back{left:648px;top:16px;width:383px;height:211px;background:var(--navy);text-align:center;color:#fff}
.value{font-size:25px;color:var(--gold);letter-spacing:.5px;line-height:1}
.value__line{font-size:8px;letter-spacing:.3px;margin-bottom:6px}
.card-back .values{padding-top:20px}
.card-back .band{top:186px;height:17px;line-height:17px;background:var(--gold);color:var(--navy);font-size:8.5px}

/* business card front */
.card-front{left:648px;top:236px;width:383px;height:217px}
.card-front .brand{right:18px;top:20px}
.person{position:absolute;left:6px;top:86px;border-left:3px solid var(--navy);padding-left:5px}
.person__name{font-size:19px;color:var(--gold);font-weight:600;line-height:1.1}
.person__role{font-size:16px;color:var(--navy);line-height:1.1}
.card-front .contact{font-size:9.6px;line-height:13px;top:156px}
.card-front .contact--left{left:5px}
.card-front .contact--right{left:219px}

/* envelope back */
.envelope-back{left:603px;top:467px;width:577px;height:251px}
.flap{position:absolute;left:0;top:0}

/* compliments slip */
.slip{left:51px;top:735px;width:541px;height:220px}
.slip .brand{left:14px;top:20px}
.slip .contact{left:440px;top:21px}
.slip .rule{left:435px;top:21px;height:44px}
.slip__note{position:absolute;right:30px;top:160px;font-family:'Cormorant Garamond',serif;font-style:italic;font-weight:500;font-size:27px;color:var(--gold)}

/* envelope front */
.envelope-front{left:603px;top:735px;width:577px;height:249px}
.envelope-front .brand{right:18px;top:21px}
.envelope-front .contact{left:9px;top:198px}
.envelope-front .rule{left:3px;top:198px;height:44px}
</style>
</head>
<body>

<section class="sheet letterhead" aria-label="Letterhead">
  <div class="brand"><span class="brand__mark"></span><span class="brand__name">Halden Marsh<span class="brand__sub">Financial Services</span></span></div>
  <span class="rule"></span>
  <div class="contact">
    Suite 4, 120-124 Harbour Road<br>Westbay NSW 2000<br>PO Box 1180 Westbay NSW 2000<br>
    <b>Tel:</b> 02 9000 1234 <b>ABN:</b> 00 000 000 000<br><b>Fax:</b> 02 9000 1235<br>
    <b>Email:</b> info@haldenmarsh.com.au<br><b>Web:</b> www.haldenmarsh.com.au
  </div>
  <div class="letter">
    <p class="letter__greet">Dear Sir / Madam,</p>
    <p class="letter__para">Lorem ipsum dolor sit amet, consectetur adipisicing elit, sed do eiusmod tempor labore et olore magna aliqua. Ut enim ad minim veniam, quis nostrud exercitation ullamco laboris nisi ut aliquip ex ea commodo consequa.Lorem ipsum dolor sit amet, nsectetur adipisicing elit, sed do eiusmod tempor incididunt ut labore et dolore magna aliqua. Ut enim ad minim veniam, quis.</p>
    <p class="letter__para">Lorem ipsum dolor sit amet, consectetur adipisicing elit, sed do eiusmod tempor labore et dolore magna aliqua. Ut enim ad minim veniam, quis nostrud exercitation ullamco laboris nisi ut aliquip ex ea commodo consequa.Lorem ipsum dolor sit amet, nsectetur adipisicing elit, sed do eiusmod tempor incididunt ut labore et dolore magna aliqua. Ut enim ad minim veniam, quis.</p>
    <p class="letter__para">Lorem ipsum dolor sit amet, consectetur adipisicing elit, sed do eiusmod tempor labore et dolore magna aliqua. Ut enim ad minim veniam, quis nostrud exercitation ullamco laboris nisi ut aliquip ex ea commodo consequa.Lorem ipsum dolor sit amet, nsectetur adipisicing elit, sed do eiusmod tempor incididunt ut labore et dolore magna aliqua. Ut enim ad minim veniam, quis.</p>
    <p class="letter__para">Lorem ipsum dolor sit amet, consectetur adipisicing elit, sed do eiusmod tempor labore et dolore magna aliqua. Ut enim ad minim veniam, quis nostrud exercitation ullamco laboris nisi ut aliquip ex ea commodo consequa.Lorem ipsum dolor sit amet, nsectetur adipisicing elit, sed do eiusmod tempor incididunt ut labore et dolore magna aliqua. Ut enim ad minim veniam, quis.</p>
    <p class="letter__para">Lorem ipsum dolor sit amet, consectetur adipisicing elit, sed do eiusmod tempor labore et dolore magna aliqua. Ut enim ad minim veniam, quis nostrud exercitation ullamco laboris nisi ut aliquip ex ea commodo consequa.Lorem ipsum dolor sit amet, nsectetur adipisicing elit, sed do eiusmod tempor incididunt ut labore et dolore magna aliqua. Ut enim ad minim veniam, quis.</p>
    <p class="letter__sign">Your Name</p>
    <p class="letter__role">Company Director</p>
  </div>
  <div class="band">Corporate Authorised Representative of Meridian Advisory Group AFSL 400000</div>
</section>

<section class="sheet card-back" aria-label="Business card, back">
  <div class="values">
    <p class="value">CERTAINTY</p><p class="value__line">DESIGNING INSURANCE SOLUTIONS</p>
    <p class="value">CLARITY</p><p class="value__line">STRATEGIC PLANNING ADVICE</p>
    <p class="value">CONFIDENCE</p><p class="value__line">CONSTRUCTING RETIREMENT PLANS</p>
  </div>
  <div class="band">Corporate Authorised Representative of Meridian Advisory Group AFSL 400000</div>
</section>

<section class="sheet card-front" aria-label="Business card, front">
  <div class="brand"><span class="brand__mark"></span><span class="brand__name">Halden Marsh<span class="brand__sub">Financial Services</span></span></div>
  <div class="person"><p class="person__name">Rowan Ellery</p><p class="person__role">Partner</p></div>
  <div class="contact contact--left">
    <b>Tel :</b> 02 9000 1234<br><b>Mob:</b> 0400 111 222<br><b>Email :</b> info@haldenmarsh.com.au<br><b>Web:</b> www.haldenmarsh.com.au
  </div>
  <div class="contact contact--right">
    Suite 4, 120-124 Harbour Road<br>Westbay NSW 2000<br>PO Box 1180 Westbay NSW 2000
  </div>
</section>

<section class="sheet envelope-back" aria-label="Envelope, back">
  <svg class="flap" width="577" height="140" viewBox="0 0 577 140">
    <path d="M0 0 H577 V20 C560 30 510 50 460 70 C380 100 330 120 288 120 C246 120 196 100 116 70 C66 50 16 30 0 20 Z" fill="var(--navy)"/>
  </svg>
</section>

<section class="sheet slip" aria-label="With compliments slip">
  <div class="brand"><span class="brand__mark"></span><span class="brand__name">Halden Marsh<span class="brand__sub">Financial Services</span></span></div>
  <span class="rule"></span>
  <div class="contact">
    Suite 4, 120-124 Harbour Road<br>Westbay NSW 2000<br>PO Box 1180 Westbay NSW 2000<br>
    <b>Tel:</b> 02 9000 1234 <b>ABN:</b> 00 000 000 000<br><b>Fax:</b> 02 9000 1235<br>
    <b>Email:</b> info@haldenmarsh.com.au<br><b>Web:</b> www.haldenmarsh.com.au
  </div>
  <p class="slip__note">with best compliments...</p>
</section>

<section class="sheet envelope-front" aria-label="Envelope, front">
  <div class="brand"><span class="brand__mark"></span><span class="brand__name">Halden Marsh<span class="brand__sub">Financial Services</span></span></div>
  <span class="rule"></span>
  <div class="contact">
    Suite 4, 120-124 Harbour Road<br>Westbay NSW 2000<br>PO Box 1180 Westbay NSW 2000<br>
    <b>Tel:</b> 02 9000 1234 <b>ABN:</b> 00 000 000 000<br><b>Fax:</b> 02 9000 1235<br>
    <b>Email:</b> info@haldenmarsh.com.au<br><b>Web:</b> www.haldenmarsh.com.au
  </div>
</section>

</body>
</html>
```